TWD OPRA Thank You card

We need a thank you card to give to our various stakeholders. The card design needs to be professional, corporate, and use elements of our current visual identity (colours and logo will be supplied). The inside of the card needs to have a space for a personal message to be written. Our target card size is 5 x 7.

As a bit of background, we fund local health care in Northvale. We do not directly provide front-line health care services. We do manage the funding and performance monitoring for the agencies we fund. We engage a wide range of people from CEO's, to MPP's, to the general public on a variety of health care topics. At the heart of it, we are a local organization that works to improve health care in Windsor/Essex, Chatham-Kent, and Sarnia/Lambton.

The final design should lean towards a more traditional look.

Industry/Entity Type

It Professional

Requirements
Must have
• It must incorporate our colour pallet and logo

```html
<!DOCTYPE html>
<html lang="en">
<head>
<meta charset="utf-8">
<title>TWD OPRA Thank You Card</title>
<link rel="stylesheet" href="https://fonts.googleapis.com/css2?family=Arimo:wght@400;700&family=Pinyon+Script&display=swap">
<style>
  :root {
    --backdrop: #d9d9d9;
    --paper: #ffffff;
    --gold: #c2b48b;
    --gold-light: #e2dac3;
    --gold-text: #b9a66e;
    --ink: #111111;
    --shadow: rgba(0, 0, 0, 0.18);
  }
  * { box-sizing: border-box; margin: 0; padding: 0; }
  html, body {
    width: 900px; height: 1200px; overflow: hidden;
    background: var(--backdrop);
    font-family: "Arimo", Arial, sans-serif;
  }
  .canvas { position: relative; width: 900px; height: 1200px; }
  .card {
    position: absolute; width: 698px; height: 498px;
    background: var(--paper);
    box-shadow: 0 3px 10px var(--shadow);
    overflow: hidden;
  }
  .card--front { left: 80px; top: 60px; }
  .card--back { left: 112px; top: 645px; }
  .card__band { position: absolute; left: 0; top: 0; width: 698px; }
  .brand {
    position: absolute; display: flex; align-items: center; gap: 10px;
    font-weight: 400; letter-spacing: -0.5px;
  }
  .brand__mark { width: 18px; height: 18px; border-radius: 50%; }
  .card--front .brand { left: 62px; top: 44px; color: var(--paper); font-size: 30px; }
  .card--front .brand__mark { background: var(--paper); }
  .greeting {
    position: absolute; left: 0; right: 0; top: 212px;
    text-align: center;
    font-family: "Pinyon Script", cursive;
    font-weight: 400;
    font-size: 92px; line-height: 1;
    color: var(--gold-text);
    text-shadow: 2px 2px 0 #2b2410;
  }
  .lockup { position: absolute; left: 262px; top: 268px; width: 236px; color: var(--ink); }
  .lockup .brand {
    position: relative; font-size: 42px; color: var(--ink);
    padding-bottom: 4px; border-bottom: 2px solid var(--ink);
  }
  .lockup .brand__mark {
    position: absolute; left: -62px; top: -26px;
    width: 44px; height: 44px; border-radius: 0; background: var(--ink);
  }
  .lockup__name { font-size: 13.5px; font-weight: 700; line-height: 1.3; padding: 6px 0 5px; border-bottom: 1px solid var(--ink); }
  .lockup__name--fr { border-bottom: none; padding-top: 4px; }
</style>
</head>
<body>
<main class="canvas">
  <section class="card card--front" aria-label="Card front">
    <svg class="card__band" height="140" viewBox="0 0 698 140" aria-hidden="true">
      <path d="M0,0 H698 V78 C560,80 470,125 300,118 C190,112 90,96 0,98 Z" fill="var(--gold-light)"/>
      <path d="M0,0 H698 V62 C560,64 470,108 300,102 C190,96 90,80 0,82 Z" fill="var(--gold)"/>
    </svg>
    <div class="brand"><span class="brand__mark"></span>Northvale</div>
    <h1 class="greeting">Thank you!</h1>
  </section>

  <section class="card card--back" aria-label="Card back">
    <svg class="card__band" height="220" viewBox="0 0 698 220" aria-hidden="true">
      <path d="M0,0 H698 V130 C560,132 460,190 300,196 C190,198 90,186 0,188 Z" fill="var(--gold-light)"/>
      <path d="M0,0 H698 V114 C560,116 460,172 300,178 C190,180 90,170 0,172 Z" fill="var(--gold)"/>
    </svg>
    <div class="lockup">
      <div class="brand"><span class="brand__mark"></span>Northvale</div>
      <p class="lockup__name">TWD OPRA Community Care<br>Funding Office</p>
      <p class="lockup__name lockup__name--fr">Bureau de financement<br>des soins communautaires<br>TWD OPRA</p>
    </div>
  </section>
</main>
</body>
</html>
```